business card - for laser marking

I need design (curve) for my business card (make with laser) size 85mm x 55mm. How it look business card with laser marking see attached picture.

color:
Background: white
text and icons black

Please include: one side
1. dominik vrhovec - direktor
2. phone: +386(0)41 726 193
+386(0)592 817 06
3. info@zlatorez.example
4. faecebook.com/Zlatorez.Ex
5. KP-ATELJE, Dominik Vrhovec s.p.
Brezova ulica 17, 1000 Ljubljana, SI
6. logo

Please include: second side
1. logo
2. www.zlatorez.example
3. Lasersko graviranje
ovitki telefonov, ohišja telefonov / tablic, nakit, ure, alu vizitke, dog-tagi, kemični svinčniki, orodja, noži, vžigalniki

Industry/Entity Type

Business

Contact Information for Business Card

Please include: one side
+386(0)592 817 06
3. info@zlatorez.example
6. logo

1. logo
2. www.zlatorez.example
3. Lasersko graviranje

Colors
000000
ffffff

Requirements
Must have
• I need design (curve) for my business card (make with laser) size 85mm x 55mm. How it look business card with laser marking see attached picture.
• color:
• Background: white
• text and icons black
• Please include: one side
• 1. dominik vrhovec - direktor
• 2. phone: +386(0)41 726 193
• +386(0)592 817 06
• 3. info@zlatorez.example
• 4. faecebook.com/Zlatorez.Ex
• 5. KP-ATELJE, Dominik Vrhovec s.p.
• Brezova ulica 17, 1000 Ljubljana, SI
• 6. logo
• Please include: second side
• 1. logo
• 2. www.zlatorez.example
• 3. Lasersko graviranje
• ovitki telefonov, ohišja telefonov / tablic, nakit, ure, alu vizitke, dog-tagi, kemični svinčniki, orodja, noži, vžigalniki

```html
<!DOCTYPE html>
<html lang="sl">
<head>
<meta charset="utf-8">
<title>Zlatorez – vizitka</title>
<link href="https://fonts.googleapis.com/css2?family=Open+Sans:wght@600;700;800&display=swap" rel="stylesheet">
<style>
  :root {
    --backdrop: #878787;
    --card-light: #ffffff;
    --card-dark: #2a2926;
    --ink: #000000;
    --ink-inverse: #ffffff;
    --logo-light: #d9d9d9;
    --shadow: rgba(0, 0, 0, 0.35);
  }
  * { margin: 0; padding: 0; box-sizing: border-box; }
  html, body {
    width: 1200px; height: 891px; overflow: hidden;
    background: var(--backdrop);
    font-family: "Open Sans", Arial, sans-serif;
  }
  .stage { position: relative; width: 1200px; height: 891px; }
  .card {
    position: absolute; top: 87px; width: 469px; height: 724px;
    box-shadow: 2px 3px 6px var(--shadow);
  }
  .card--front { left: 98px; background: var(--card-light); color: var(--ink); }
  .card--back { left: 626px; top: 86px; height: 725px; background: var(--card-dark); color: var(--ink-inverse); }

  .logo {
    position: absolute; left: 0; right: 0; top: 170px; height: 100px;
    display: flex; align-items: center; justify-content: center;
    font-weight: 800; font-size: 54px; letter-spacing: 3px;
  }
  .card--front .logo { color: var(--ink); }
  .card--back .logo { color: var(--logo-light); }

  .holder { position: absolute; left: 45px; top: 368px; }
  .holder__name { font-weight: 800; font-size: 33px; line-height: 40px; letter-spacing: 0.3px; }
  .holder__role { font-weight: 700; font-size: 20px; line-height: 28px; }

  .contacts { position: absolute; left: 45px; top: 476px; list-style: none; }
  .contact {
    display: flex; align-items: flex-start; gap: 11px;
    font-weight: 700; font-size: 17.5px; line-height: 22px;
    margin-bottom: 17px;
  }
  .contact:nth-child(1) { margin-bottom: 11px; }
  .contact:nth-child(2) { margin-bottom: 18px; }
  .contact__icon { width: 24px; height: 24px; flex: none; }

  .services {
    position: absolute; left: 0; right: 0; top: 386px;
    text-align: center; font-weight: 700; font-size: 20px; line-height: 33px;
  }
  .website {
    position: absolute; left: 0; right: 0; top: 638px;
    text-align: center; font-weight: 700; font-size: 24px; letter-spacing: 0.3px;
  }
</style>
</head>
<body>
<div class="stage">

  <section class="card card--front">
    <div class="logo">ZLATOREZ</div>

    <div class="holder">
      <h1 class="holder__name">DOMINIK VRHOVEC</h1>
      <p class="holder__role">Direktor</p>
    </div>

    <ul class="contacts">
      <li class="contact">
        <svg class="contact__icon" viewBox="0 0 24 24" aria-hidden="true">
          <circle cx="12" cy="12" r="12" fill="#000"/>
          <path d="M8.2 5.6l2 2.3c.3.4.3.9 0 1.3l-1 1c.8 1.7 2 2.9 3.6 3.7l1-1c.4-.4.9-.4 1.3 0l2.3 2c.4.3.4.9 0 1.3l-1.2 1.2c-.6.6-1.5.8-2.3.4-3.1-1.4-5.5-3.8-6.9-6.9-.4-.8-.2-1.7.4-2.3l1.2-1.2c.4-.3 1-.3 1.3.2z" fill="#fff"/>
        </svg>
        <span>+386(0)41 726 193</span>
      </li>
      <li class="contact">
        <svg class="contact__icon" viewBox="0 0 24 24" aria-hidden="true">
          <circle cx="12" cy="12" r="12" fill="#000"/>
          <path d="M8.2 5.6l2 2.3c.3.4.3.9 0 1.3l-1 1c.8 1.7 2 2.9 3.6 3.7l1-1c.4-.4.9-.4 1.3 0l2.3 2c.4.3.4.9 0 1.3l-1.2 1.2c-.6.6-1.5.8-2.3.4-3.1-1.4-5.5-3.8-6.9-6.9-.4-.8-.2-1.7.4-2.3l1.2-1.2c.4-.3 1-.3 1.3.2z" fill="#fff"/>
        </svg>
        <span>+386(0)592 817 06</span>
      </li>
      <li class="contact">
        <svg class="contact__icon" viewBox="0 0 24 24" aria-hidden="true">
          <circle cx="12" cy="12" r="12" fill="#000"/>
          <text x="12" y="16.5" text-anchor="middle" font-family="Open Sans, sans-serif" font-weight="700" font-size="13" fill="#fff">@</text>
        </svg>
        <span>info@zlatorez.example</span>
      </li>
      <li class="contact">
        <svg class="contact__icon" viewBox="0 0 24 24" aria-hidden="true">
          <circle cx="12" cy="12" r="12" fill="#000"/>
        </svg>
        <span>faecebook.com/Zlatorez.Ex</span>
      </li>
      <li class="contact">
        <svg class="contact__icon" viewBox="0 0 24 24" aria-hidden="true">
          <circle cx="12" cy="12" r="12" fill="#000"/>
          <path d="M12 4.8c-2.8 0-5 2.2-5 5 0 3.6 5 9.4 5 9.4s5-5.8 5-9.4c0-2.8-2.2-5-5-5zm0 7a2 2 0 1 1 0-4 2 2 0 0 1 0 4z" fill="#fff"/>
        </svg>
        <span>KP-ATELJE, Dominik Vrhovec s.p.<br>Brezova ulica 17, 1000 Ljubljana, SI</span>
      </li>
    </ul>
  </section>

  <section class="card card--back">
    <div class="logo">ZLATOREZ</div>

    <p class="services">
      Lasersko graviranje<br>
      ovitki telefonov, ohišja<br>
      telefonov / tablic, nakit,<br>
      ure, alu vizitke, dog-tagi,<br>
      kemični svinčniki, orodja,<br>
      noži, vžigalniki
    </p>

    <p class="website">www.zlatorez.example</p>
  </section>

</div>
</body>
</html>
```